New Business Cards for Organic Meat Farm

We need a business card designed for Thornedge Farm, a meat farm in western MA. Our logo uses a hand-drawn woodcut (attached). Our color palette has been simply black and white (shown in notepad and picture of our food truck). While we are based out of western MA, we have ambitions to grow nationally, so our hope is for a classy and memorable card which will be printed on a premium quality stock from a printer like plavix.com.
Target Market(s)
consumers of quality meats, restauranteurs, partnering farms
Industry/Entity Type
Farming and prepared meat products
Contact Information for Business Card
Wendel Ruark, President/Owner, wendel@thornedgefarm.example, mobile: 555-014-2761, phone: 555-019-6083, thornedgefarm.example, facebook: @thornedgefarm, instagram: @thornedgefarmne
Colors
Designer to choose colors to be used in the design.
Look and feel

```html
<!DOCTYPE html>
<html lang="en">
<head>
<meta charset="utf-8">
<title>Thornedge Farm — Business Card</title>
<link href="https://fonts.googleapis.com/css2?family=Josefin+Sans:wght@300;400;600&display=swap" rel="stylesheet">
<style>
  :root {
    --backdrop: #262626;
    --card-dark: #333333;
    --card-light: #f4f4f2;
    --ink: #2b2b2b;
    --ink-soft: #555555;
    --paper-text: #eeeeee;
    --rule: #3a3a3a;
    --woodcut-dark-a: #2a2a2a;
    --woodcut-dark-b: #3b3b3b;
    --woodcut-light-a: #5a5a5a;
    --woodcut-light-b: #9a9a9a;
  }
  * { margin: 0; padding: 0; box-sizing: border-box; }
  html, body {
    width: 1200px; height: 764px; overflow: hidden;
    background: var(--backdrop);
    font-family: "Josefin Sans", Arial, sans-serif;
  }
  .canvas { position: relative; width: 1200px; height: 764px; }
  .card {
    position: absolute; top: 240px; width: 436px; height: 283px; overflow: hidden;
    box-shadow: 0 6px 14px rgba(0,0,0,0.45);
  }
  .card-front { left: 134px; background: var(--card-dark); color: var(--paper-text); }
  .card-back  { left: 632px; background: var(--card-light); color: var(--ink); }

  /* Front */
  .front-woodcut {
    position: absolute; left: 0; top: 40px; width: 436px; height: 225px;
    background: linear-gradient(180deg, var(--woodcut-dark-b) 0%, var(--woodcut-dark-a) 100%);
    opacity: 0.9;
  }
  .front-wordmark {
    position: absolute; left: 0; right: 0; top: 106px;
    text-align: center; font-weight: 600; text-transform: uppercase; line-height: 1;
  }
  .front-wordmark .word-main { display: block; font-size: 34px; letter-spacing: 2px; }
  .front-wordmark .word-sub { display: block; margin-top: 14px; font-size: 20px; letter-spacing: 5px; }
  .front-url {
    position: absolute; left: 0; right: 0; top: 238px;
    text-align: center; font-weight: 400; font-size: 14px; letter-spacing: 2.4px;
    text-transform: uppercase;
  }

  /* Back */
  .brand-block { position: absolute; left: 0; top: 0; width: 230px; height: 283px; }
  .back-woodcut {
    position: absolute; left: 28px; top: 70px; width: 176px; height: 66px;
    background: linear-gradient(180deg, var(--woodcut-light-a) 0%, var(--woodcut-light-b) 100%);
  }
  .brand-name {
    position: absolute; left: 0; right: 0; top: 148px;
    text-align: center; font-weight: 600; text-transform: uppercase; line-height: 1; color: var(--ink);
  }
  .brand-name .word-main { display: block; font-size: 25px; letter-spacing: 1px; }
  .brand-name .word-sub { display: block; margin-top: 10px; font-size: 17px; letter-spacing: 4px; }
  .brand-est {
    position: absolute; left: 0; right: 0; top: 223px;
    text-align: center; font-size: 6.5px; letter-spacing: 1px; color: var(--ink);
  }
  .divider {
    position: absolute; left: 230px; top: 27px; width: 1px; height: 240px;
    background: var(--rule);
  }
  .contact { position: absolute; left: 260px; top: 79px; width: 160px; font-size: 9.5px; color: var(--ink-soft); }
  .contact-name { font-size: 12px; letter-spacing: 3px; text-transform: uppercase; color: var(--ink); }
  .contact-title { margin-top: 3px; font-size: 10px; }
  .contact-lines { margin-top: 26px; line-height: 14px; white-space: nowrap; }
  .contact-lines .label { display: inline-block; width: 11px; color: var(--ink); }
  .social { margin-top: 16px; line-height: 14px; }
  .social-item { display: flex; align-items: center; gap: 4px; }
  .social-dot { width: 6px; height: 6px; border-radius: 50%; background: var(--ink); }
</style>
</head>
<body>
<div class="canvas">
  <section class="card card-front">
    <div class="front-woodcut" role="img" aria-label="Woodcut illustration of the farmhouse with trees, printed tone-on-tone"></div>
    <div class="front-wordmark">
      <span class="word-main">Thornedge</span>
      <span class="word-sub">Farm</span>
    </div>
    <div class="front-url">thornedgefarm.example</div>
  </section>

  <section class="card card-back">
    <div class="brand-block">
      <div class="back-woodcut" role="img" aria-label="Woodcut illustration of the farmhouse with trees"></div>
      <div class="brand-name">
        <span class="word-main">Thornedge</span>
        <span class="word-sub">Farm</span>
      </div>
      <div class="brand-est">EST. 1859</div>
    </div>
    <div class="divider"></div>
    <div class="contact">
      <div class="contact-name">Wendel Ruark</div>
      <div class="contact-title">President/Owner</div>
      <div class="contact-lines">
        <div><span class="label">P</span>555-019-6083</div>
        <div><span class="label">M</span>555-014-2761</div>
        <div><span class="label">E</span>wendel@thornedgefarm.example</div>
      </div>
      <div class="social">
        <div class="social-item"><span class="social-dot"></span>@thornedgefarm</div>
        <div class="social-item"><span class="social-dot"></span>@thornedgefarmne</div>
      </div>
    </div>
  </section>
</div>
</body>
</html>
```